A Hair, Beauty and Nails Wholesalers Needs a Business Card Design

We need a business card design for our company which is being passed from parents to daughter, so we wont to re-launch the company with an updated, modern, sophisticated, elegant, chic and fresh look which still incorporates the original colour scheme of Hot Pink, Dark Grey and White. The original logo which is attached can be used on the card but we would like to see some designs with the logo and some without, as we have not yet decided if we want the logo on the card. The name of our company is 'RM's Distributors' and the name of our website is RM's GlowandPolish.example.au. We specialise in supplying a massive range of Hair, Beauty and Nail products to the industry. We are based in QLD, Australia but ship many orders via our website all across Australia.

Industry/Entity Type

Business

```html
<!DOCTYPE html>
<html lang="en">
<head>
<meta charset="utf-8">
<title>RM's Distributors – Business Card</title>
<link rel="stylesheet" href="https://fonts.googleapis.com/css2?family=Open+Sans:wght@400;600&display=swap">
<style>
  :root {
    --hot-pink: #e20a7f;
    --dark-grey: #9a9a9a;
    --stage: #2f2f2f;
    --white: #ffffff;
    --ink: #1a1a1a;
  }
  * { margin: 0; padding: 0; box-sizing: border-box; }
  html, body {
    width: 960px; height: 1200px; overflow: hidden;
    background: var(--stage);
    font-family: "Open Sans", Arial, sans-serif;
  }
  .canvas { position: relative; width: 960px; height: 1200px; }

  .card { position: absolute; width: 661px; height: 387px; overflow: hidden; }

  /* Front */
  .card-front { left: 146px; top: 136px; background: var(--hot-pink); }
  .front-motif {
    position: absolute; left: 68px; top: 32px; width: 506px; height: 334px;
    background: radial-gradient(ellipse at 40% 50%, rgba(160,50,108,0.55), rgba(160,50,108,0) 72%);
  }
  .front-url {
    position: absolute; right: 60px; top: 336px;
    color: var(--white); font-size: 15px; letter-spacing: 0.1px;
  }

  /* Back */
  .card-back { left: 161px; top: 680px; background: var(--white); }
  .brand {
    position: absolute; left: 62px; top: 176px;
    display: flex; align-items: center; gap: 8px;
  }
  .brand-mark { width: 14px; height: 14px; border-radius: 50%; background: var(--hot-pink); }
  .brand-name { color: var(--hot-pink); font-size: 19px; font-weight: 600; line-height: 24px; }

  .contact { position: absolute; right: 59px; top: 186px; text-align: right; color: var(--ink); }
  .contact-name { color: var(--hot-pink); font-size: 16px; line-height: 20px; }
  .contact-role { font-size: 10.5px; line-height: 14px; }
  .contact-details { margin-top: 38px; font-size: 11px; line-height: 15.6px; }

  .swoosh { position: absolute; left: 0; top: 0; width: 661px; height: 387px; }
</style>
</head>
<body>
<main class="canvas">
  <section class="card card-front">
    <div class="front-motif" role="img" aria-label="Large decorative motif area in darker pink"></div>
    <p class="front-url">www.glowandpolish.example.au</p>
  </section>

  <section class="card card-back">
    <svg class="swoosh" viewBox="0 0 661 387" aria-hidden="true">
      <path d="M0 238 C90 318 260 380 480 386 L661 387 L0 387 Z" fill="var(--dark-grey)"/>
      <path d="M0 264 C95 332 262 382 480 386 L661 387 L0 387 Z" fill="var(--white)"/>
      <path d="M0 280 C100 345 262 385 480 386 L661 374 L661 387 L0 387 Z" fill="var(--hot-pink)"/>
    </svg>

    <div class="brand">
      <span class="brand-mark"></span>
      <span class="brand-name">RM's GlowandPolish</span>
    </div>

    <div class="contact">
      <p class="contact-name">Tamsin Ridgeway</p>
      <p class="contact-role">Manager</p>
      <div class="contact-details">
        <p>RM's Distributors</p>
        <p>128 Example Street</p>
        <p>SPRINGVALE, QLD, 4000</p>
        <p>Ph: (07) 4000 0123</p>
        <p>Email: admin@glowandpolish.example.au</p>
      </div>
    </div>
  </section>
</main>
</body>
</html>
```